professional business card

Professional business card with logo on one side, and underneath logo list:
- power
-data
-fibre optic
-isolar

On other side:
Marcus Trent
Owner
MOB 0492 738 204
marcus@vorpa.com.au
www.vorpaelectrical.com.au

Please edit logo to just leave VORPA

```html
<!DOCTYPE html>
<html lang="en">
<head>
<meta charset="utf-8">
<title>VORPA Business Card</title>
<link rel="stylesheet" href="https://fonts.googleapis.com/css2?family=Work+Sans:wght@400;500;600&display=swap">
<style>
  :root {
    --teal: #17a0a0;
    --grey-card: #7b7c7e;
    --grey-text: #6d6e70;
    --grey-band: #8c8d8f;
    --white: #ffffff;
    --page: #ececec;
  }
  * { box-sizing: border-box; margin: 0; padding: 0; }
  html, body { width: 1200px; height: 900px; overflow: hidden; }
  body {
    background: var(--page);
    font-family: "Work Sans", Arial, sans-serif;
    position: relative;
  }
  .card {
    position: absolute;
    left: 250px;
    width: 700px;
    height: 400px;
    border-radius: 26px;
    overflow: hidden;
    box-shadow: 0 6px 18px rgba(0,0,0,0.18);
  }
  .card-front { top: 36px; background: var(--white); }
  .card-back { top: 464px; background: var(--grey-card); }

  .holder { position: absolute; left: 48px; top: 46px; }
  .holder-name {
    color: var(--teal);
    font-size: 31px;
    font-weight: 500;
    letter-spacing: 1.5px;
    text-transform: uppercase;
  }
  .holder-role {
    color: var(--grey-text);
    font-size: 17px;
    margin-top: 2px;
  }
  .divider {
    position: absolute;
    left: 48px; right: 0;
    top: 130px;
    height: 2px;
    background: var(--teal);
  }
  .contacts {
    position: absolute;
    left: 48px; top: 150px;
    list-style: none;
  }
  .contacts li {
    display: flex; align-items: center; gap: 10px;
    color: var(--grey-text);
    font-size: 17px;
    line-height: 28px;
  }
  .contacts svg { width: 13px; height: 13px; flex: none; }

  .brand {
    position: absolute;
    right: 60px; top: 168px;
    width: 290px;
    text-align: center;
  }
  .brand-name {
    color: var(--teal);
    font-size: 76px;
    font-weight: 600;
    letter-spacing: 4px;
    line-height: 1;
  }
  .services {
    list-style: none;
    display: flex;
    justify-content: center;
    gap: 10px;
    margin-top: 10px;
    color: var(--grey-text);
    font-size: 13px;
    font-weight: 500;
    letter-spacing: 1.2px;
    text-transform: uppercase;
  }
  .services li { display: flex; align-items: center; gap: 10px; }
  .services li + li::before {
    content: "";
    width: 5px; height: 5px;
    background: var(--teal);
    border-radius: 50%;
  }
  .address {
    position: absolute;
    right: 48px; bottom: 36px;
    text-align: right;
    color: var(--grey-text);
    font-size: 17px;
    line-height: 25px;
  }
  .footer-band { position: absolute; left: 0; bottom: 0; width: 700px; height: 110px; }

  .back-watermark {
    position: absolute;
    left: -20px; top: 60px;
    color: rgba(255,255,255,0.12);
    font-size: 300px;
    font-weight: 500;
    line-height: 1;
    letter-spacing: 6px;
    white-space: nowrap;
  }
  .back-name {
    position: absolute;
    left: 0; right: 0; top: 140px;
    text-align: center;
    color: var(--white);
    font-size: 96px;
    font-weight: 600;
    letter-spacing: 6px;
    line-height: 1;
  }
</style>
</head>
<body>
  <section class="card card-front">
    <div class="holder">
      <p class="holder-name">Marcus Trent</p>
      <p class="holder-role">Owner</p>
    </div>
    <div class="divider"></div>
    <ul class="contacts">
      <li>
        <svg viewBox="0 0 16 16" aria-hidden="true"><path fill="#17a0a0" d="M4 1l3 3-2 2c1 2 3 4 5 5l2-2 3 3-2 2C7 14 2 9 2 3z"/></svg>
        0492 738 204
      </li>
      <li>
        <svg viewBox="0 0 16 16" aria-hidden="true"><rect x="1.5" y="3.5" width="13" height="9" fill="none" stroke="#17a0a0" stroke-width="1.6"/><path d="M1.5 4l6.5 5 6.5-5" fill="none" stroke="#17a0a0" stroke-width="1.6"/></svg>
        marcus@vorpa.com.au
      </li>
      <li>
        <svg viewBox="0 0 16 16" aria-hidden="true"><circle cx="8" cy="8" r="6.5" fill="none" stroke="#17a0a0" stroke-width="1.5"/><ellipse cx="8" cy="8" rx="2.8" ry="6.5" fill="none" stroke="#17a0a0" stroke-width="1.2"/><path d="M1.5 8h13" stroke="#17a0a0" stroke-width="1.2"/></svg>
        www.vorpaelectrical.com.au
      </li>
    </ul>
    <div class="brand">
      <p class="brand-name">VORPA</p>
      <ul class="services">
        <li>Power</li>
        <li>Data</li>
        <li>Fibre Optic</li>
        <li>Solar</li>
      </ul>
    </div>
    <p class="address">1870 Harlow Avenue<br>Dunmore, NSW 2529</p>
    <svg class="footer-band" viewBox="0 0 700 110" aria-hidden="true">
      <path d="M0 14 L300 78 Q330 84 360 84 Q395 84 420 110 L0 110 Z" fill="var(--grey-band)"/>
      <path d="M0 6 L290 68" stroke="var(--teal)" stroke-width="6" fill="none"/>
    </svg>
  </section>

  <section class="card card-back">
    <p class="back-watermark" aria-hidden="true">VORPA</p>
    <p class="back-name">VORPA</p>
  </section>
</body>
</html>
```